Logo needed for business card

Velquist Pty Ltd is in the business of healthcare and ecommerce.

We own and manage pharmacies and online health ecomerce sites.

We provide ecommerce consultants for companies looking for an ecommerce business startegy.

Think of it as the umbrella under which several healthcare brands may sit.

When I think of Velquist, I visulaise slick black/metalic colours, so please stay away from the common blue and green colours that seem to be so popular in this field.

Target Market(s)

CEOs and COOs

Industry/Entity Type

Healthcare

Contact Information for Business Card

Tessa Lindqvist
Director
Velquist Pty Ltd
4/362 Fennick Pde
Brellton, NSW 2148

Requirements
Must have
• Design must have scope to be implemented on the company's website and letterheads etc.

```html
<!DOCTYPE html>
<html lang="en">
<head>
<meta charset="utf-8">
<title>Velquist Pty Ltd — Business Card</title>
<link rel="stylesheet" href="https://fonts.googleapis.com/css2?family=Jost:wght@300;400;500;600&display=swap">
<style>
  :root {
    --page-bg: #ffffff;
    --card-dark: #1c1c20;
    --card-mid: #26262b;
    --text-light: #f2f2f2;
    --metal-grey: #9d9ea1;
  }
  html, body {
    margin: 0;
    padding: 0;
    width: 1200px;
    height: 1000px;
    overflow: hidden;
    background: var(--page-bg);
  }
  .canvas {
    position: relative;
    width: 1200px;
    height: 1000px;
    font-family: "Jost", sans-serif;
  }
  .business-card {
    position: absolute;
    left: 165px;
    top: 227px;
    width: 841px;
    height: 518px;
    background: linear-gradient(90deg, var(--card-dark), var(--card-mid) 50%, var(--card-dark));
  }
  .contact-name {
    position: absolute;
    left: 334px;
    top: 46px;
    margin: 0;
    font-size: 30px;
    font-weight: 500;
    color: var(--text-light);
    line-height: 1;
  }
  .contact-role {
    position: absolute;
    left: 334px;
    top: 84px;
    margin: 0;
    font-size: 26px;
    font-weight: 300;
    color: var(--text-light);
    line-height: 1;
  }
  .brand-mark {
    position: absolute;
    left: 188px;
    top: 310px;
  }
  .brand-divider {
    position: absolute;
    left: 315px;
    top: 310px;
    width: 1px;
    height: 104px;
    background: var(--metal-grey);
  }
  .brand-name {
    position: absolute;
    left: 333px;
    top: 296px;
    margin: 0;
    font-size: 44px;
    font-weight: 600;
    color: var(--metal-grey);
    line-height: 1;
    white-space: nowrap;
  }
  .brand-address {
    position: absolute;
    left: 333px;
    top: 350px;
    margin: 0;
    font-size: 29px;
    font-weight: 400;
    color: var(--text-light);
    line-height: 34px;
    font-style: normal;
  }
</style>
</head>
<body>
<div class="canvas">
  <section class="business-card" role="img" aria-label="Dark charcoal linen-textured card background">
    <h1 class="contact-name">Tessa Lindqvist</h1>
    <p class="contact-role">Director</p>

    <svg class="brand-mark" width="106" height="106" viewBox="0 0 106 106" aria-hidden="true">
      <circle cx="53" cy="53" r="52" fill="var(--metal-grey)"/>
    </svg>
    <div class="brand-divider"></div>
    <p class="brand-name">velquist pty ltd</p>
    <address class="brand-address">4/362 Fennick Pde Brellton,<br>NSW 2148</address>
  </section>
</div>
</body>
</html>
```